Capacity building in Resource Management

Need design of a business card (later to be completed by letterhead and webdesign in same fashion) for a professional who works in the field of capacity building of professionals in mostly developing countries in the field waste/resource management, waste prevention/reduction, cleaner production, stakeholders involvement, etc.
Info on business cards is to include provided logo, info in provided file and picture.

Industry/Entity Type

Business

Contact Information for Business Card

White background

Font styles to use
Sans Serif

Colors

Designer to choose colors to be used in the design.

```html
<!DOCTYPE html>
<html lang="en">
<head>
<meta charset="utf-8">
<title>terra-learna business card</title>
<link rel="stylesheet" href="https://fonts.googleapis.com/css2?family=Lato:wght@300;400;700&display=swap">
<style>
  :root {
    --backdrop: #e9e7e4;
    --card: #121212;
    --card-edge: #1c1c1c;
    --ink: #f2f2f2;
    --muted: #9a9a9a;
    --accent: #5aa545;
    --rule: #4a4a4a;
  }
  * { box-sizing: border-box; margin: 0; padding: 0; }
  html, body { width: 1200px; height: 900px; overflow: hidden; }
  body {
    background: var(--backdrop);
    font-family: "Lato", Arial, sans-serif;
    color: var(--ink);
    position: relative;
  }
  .card {
    position: absolute;
    top: 302px;
    width: 520px;
    height: 297px;
    background: var(--card);
    border: 1px solid var(--card-edge);
    border-radius: 4px;
    overflow: hidden;
    box-shadow: 0 10px 24px rgba(0,0,0,.25);
  }
  .card--contact { left: 60px; }
  .card--brand { left: 620px; }

  /* contact side */
  .portrait {
    position: absolute;
    right: 0; top: 0;
    width: 250px; height: 297px;
    background: radial-gradient(ellipse at 40% 35%, #8a6a58 0%, #4a3a32 28%, rgba(18,18,18,0) 55%),
                radial-gradient(ellipse at 65% 95%, #e6e6e6 0%, #bdbdbd 30%, rgba(18,18,18,0) 62%),
                var(--card);
  }
  .contact-block {
    position: absolute;
    left: 26px;
    font-size: 13.5px;
    line-height: 19px;
    font-weight: 400;
  }
  .contact-block--direct { top: 34px; }
  .contact-block--address { top: 110px; padding-left: 14px; font-size: 15px; line-height: 19px; }
  .contact-block--social { top: 180px; font-size: 15.5px; line-height: 24px; }
  .row { display: flex; align-items: center; gap: 7px; white-space: nowrap; }
  .icon-small { width: 11px; height: 11px; flex: none; }
  .icon-social {
    width: 19px; height: 19px; flex: none;
    border: 1.6px solid var(--accent);
    border-radius: 50%;
  }

  /* brand side */
  .brand {
    position: absolute;
    right: 50px; top: 70px;
    text-align: right;
  }
  .brand-name {
    font-size: 40px;
    font-weight: 700;
    color: var(--accent);
    letter-spacing: .5px;
    line-height: 1;
    display: flex; align-items: center; gap: 10px; justify-content: flex-end;
  }
  .brand-dot { width: 16px; height: 16px; border-radius: 50%; background: var(--accent); }
  .brand-tagline {
    margin-top: 6px;
    font-size: 12px;
    color: var(--muted);
    letter-spacing: .3px;
  }
  .divider {
    position: absolute;
    left: 40px; right: 40px; top: 170px;
    height: 1px;
    background: var(--rule);
  }
  .services {
    position: absolute;
    left: 40px; right: 40px; top: 186px;
    text-align: center;
    font-size: 14.5px;
    font-weight: 300;
    color: var(--muted);
    line-height: 22px;
  }
  .services .sep { margin: 0 6px; }
</style>
</head>
<body>

<section class="card card--contact">
  <div class="portrait" role="img" aria-label="Portrait photograph of the consultant in a white shirt against a black background"></div>

  <div class="contact-block contact-block--direct">
    <div class="row">
      <svg class="icon-small" viewBox="0 0 12 12"><rect x="1" y="3" width="10" height="7" rx="1.5" fill="var(--accent)"/><rect x="2" y="1" width="8" height="3" rx="1.5" fill="var(--accent)"/></svg>
      <span>+49 1523 447 2190</span>
    </div>
    <div class="row">
      <svg class="icon-small" viewBox="0 0 12 12"><rect x="1" y="2.5" width="10" height="7" fill="var(--accent)"/><path d="M1 2.5 L6 7 L11 2.5" fill="none" stroke="var(--card)" stroke-width="1"/></svg>
      <span>jonas.verhoef@terra-learna.com</span>
    </div>
    <div class="row">
      <svg class="icon-small" viewBox="0 0 12 12"><circle cx="6" cy="6" r="5" fill="var(--accent)"/></svg>
      <span>www.terra-learna.com</span>
    </div>
  </div>

  <div class="contact-block contact-block--address">
    <div>Lindenhofweg 12</div>
    <div>10117 Berlin</div>
    <div>Germany</div>
  </div>

  <div class="contact-block contact-block--social">
    <div class="row"><span class="icon-social"></span><span>+49 1523 447 2190</span></div>
    <div class="row"><span class="icon-social"></span><span>@jonasverhoef</span></div>
    <div class="row"><span class="icon-social"></span><span>verhoef1998</span></div>
    <div class="row"><span class="icon-social"></span><span>Jonas Verhoef</span></div>
  </div>
</section>

<section class="card card--brand">
  <div class="brand">
    <div class="brand-name"><span class="brand-dot"></span>terra-learna</div>
    <div class="brand-tagline">capacity building in resource management</div>
  </div>
  <div class="divider"></div>
  <div class="services">
    <div>Field waste/resource management<span class="sep">|</span>Waste prevention/reduction</div>
    <div>Cleaner production<span class="sep">|</span>Stakeholders involvement</div>
  </div>
</section>

</body>
</html>
```